Business Card Design for Online Gift Business

Business card design for a new online Canadian company called "Harlow & Reed Gift Crates" selling modern and luxurious gift boxes for every occasion. Items are sourced locally from talented socially-responsible Canadian artisans. Each gift is elegantly presented in a keepsake wood box to ensure a lasting impression.

Industry/Entity Type

E-Commerce

Contact Information for Business Card

Merin Holloway, Proprietor
Alder Falls, AB
587-214-3306
www.harlowandreed.ca
hello@harlowandreed.ca

Requirements
Must have
• Gifts from our best, to your best
• Please also include the symbols for Kinfeed and Snapwell
Nice to have
• **I have attached a few samples of background colors and font colors that I like. I hope this helps in a few directions to try.

```html
<!DOCTYPE html>
<html lang="en">
<head>
<meta charset="utf-8">
<title>Harlow &amp; Reed Gift Crates – Business Card</title>
<link rel="stylesheet" href="https://fonts.googleapis.com/css2?family=Cabin:wght@400;500&family=Pinyon+Script&display=swap">
<style>
  :root {
    --backdrop: #8f8f8f;
    --paper: #e0dfdf;
    --charcoal: #323232;
    --gold: #bfa06c;
    --gold-shade: #a98c5c;
    --ink: #2e2e2e;
    --on-gold: #f3ede2;
  }
  * { margin: 0; padding: 0; box-sizing: border-box; }
  html, body { width: 980px; height: 1200px; overflow: hidden; }
  body {
    position: relative;
    background: var(--backdrop);
    font-family: "Cabin", sans-serif;
  }
  .card {
    position: absolute;
    background: var(--paper);
    box-shadow: 0 14px 18px -10px rgba(0,0,0,0.45);
    overflow: hidden;
  }
  .card--front { left: 126px; top: 131px; width: 714px; height: 410px; }
  .card--back  { left: 119px; top: 710px; width: 714px; height: 412px; }

  .wordmark {
    position: absolute;
    display: flex;
    align-items: center;
    gap: 14px;
    color: var(--gold);
    font-weight: 400;
    white-space: nowrap;
    line-height: 1;
  }
  .wordmark__dot { border-radius: 50%; background: var(--gold); flex: none; }
  .card--front .wordmark { left: 0; right: 0; top: 90px; justify-content: center; font-size: 70px; }
  .card--front .wordmark__dot { width: 22px; height: 22px; }
  .card--back .wordmark { left: 35px; top: 56px; font-size: 44px; gap: 10px; }
  .card--back .wordmark__dot { width: 14px; height: 14px; }

  .band-dark { position: absolute; left: 0; right: 0; background: var(--charcoal); }
  .card--front .band-dark { top: 303px; bottom: 0; }

  .ribbon { position: absolute; background: var(--gold); }
  .ribbon-center {
    position: absolute;
    background: var(--gold);
    box-shadow: -5px 0 0 var(--gold-shade), 5px 0 0 var(--gold-shade);
  }
  .card--front .ribbon { left: 46px; top: 267px; width: 619px; height: 69px; }
  .card--front .ribbon-center { left: 287px; top: 275px; width: 140px; height: 64px; }

  .social {
    position: absolute;
    top: 292px;
    display: flex;
    align-items: center;
    gap: 8px;
    color: var(--on-gold);
    font-size: 15px;
    line-height: 26px;
  }
  .social--left { left: 50px; }
  .social--right { right: 52px; }
  .social__dot { width: 26px; height: 26px; border-radius: 50%; background: var(--on-gold); }

  .tagline {
    position: absolute;
    left: 0; right: 0; top: 346px;
    text-align: center;
    font-family: "Pinyon Script", cursive;
    font-size: 38px;
    line-height: 50px;
    color: var(--gold);
  }

  .holder { position: absolute; left: 442px; top: 18px; width: 260px; text-align: center; color: var(--ink); }
  .holder__name { font-size: 29px; font-weight: 400; line-height: 36px; }
  .holder__role { font-size: 22px; line-height: 28px; margin-top: 0; }

  .card--back .band-dark { top: 176px; height: 77px; }
  .contact-phone { position: absolute; left: 57px; top: 194px; font-size: 25px; line-height: 28px; color: var(--gold); }
  .contact-online { position: absolute; left: 437px; top: 185px; width: 260px; text-align: center; font-size: 20px; line-height: 28px; color: var(--gold); }

  .card--back .ribbon { left: 0; right: 0; top: 253px; height: 61px; }
  .card--back .ribbon-center { left: 273px; top: 260px; width: 168px; height: 58px; }

  .icon { position: absolute; top: 266px; width: 36px; height: 36px; }
  .icon--phone { left: 105px; }
  .icon--pin { left: 337px; top: 264px; width: 40px; height: 40px; }
  .icon--web { left: 541px; }

  .location { position: absolute; left: 0; right: 0; top: 334px; text-align: center; font-size: 25px; line-height: 30px; color: var(--ink); }
  .edge-bar { position: absolute; left: 146px; width: 421px; bottom: 0; height: 6px; background: var(--gold); }
</style>
</head>
<body>

<section class="card card--front" aria-label="Card front">
  <div class="wordmark"><span class="wordmark__dot"></span><span>Harlow &amp; Reed</span></div>
  <div class="band-dark"></div>
  <div class="ribbon"></div>
  <div class="ribbon-center"></div>
  <div class="social social--left"><span class="social__dot"></span><span>Kinfeed</span></div>
  <div class="social social--right"><span>Snapwell</span><span class="social__dot"></span></div>
  <p class="tagline">Gifts from our best, to your best</p>
</section>

<section class="card card--back" aria-label="Card back">
  <div class="wordmark"><span class="wordmark__dot"></span><span>Harlow &amp; Reed</span></div>
  <div class="holder">
    <p class="holder__name">Merin Holloway</p>
    <p class="holder__role">Proprietor</p>
  </div>
  <div class="band-dark"></div>
  <p class="contact-phone">587-214-3306</p>
  <p class="contact-online">hello@harlowandreed.ca<br>www.harlowandreed.ca</p>
  <div class="ribbon"></div>
  <div class="ribbon-center"></div>

  <svg class="icon icon--phone" viewBox="0 0 24 24" aria-hidden="true">
    <path fill="#323232" d="M6.6 2.5c.6-.3 1.3-.1 1.6.5l1.8 3.4c.3.6.2 1.2-.3 1.6L8.3 9c.9 2.3 2.6 4.1 4.8 5.2l1.1-1.3c.4-.5 1.1-.6 1.6-.3l3.3 1.9c.6.3.8 1 .5 1.6l-1 2c-.5 1-1.6 1.5-2.7 1.3C9.6 18.2 5.2 13.4 4.4 7.1c-.1-1 .4-2 1.3-2.5z"/>
  </svg>
  <svg class="icon icon--pin" viewBox="0 0 40 40" aria-hidden="true">
    <path fill="#323232" d="M24 2a8 8 0 0 0-8 8c0 6 8 14 8 14s8-8 8-14a8 8 0 0 0-8-8zm0 4.5a3.5 3.5 0 1 1 0 7 3.5 3.5 0 0 1 0-7z"/>
    <path fill="#323232" d="M4 26l8-4 6 2-3 14H1zm14 12l3-12 5 2 12-2-2 12z"/>
  </svg>
  <svg class="icon icon--web" viewBox="0 0 36 36" aria-hidden="true">
    <g fill="none" stroke="#323232" stroke-width="1.6">
      <circle cx="18" cy="18" r="16"/>
      <ellipse cx="18" cy="18" rx="7" ry="16"/>
      <line x1="18" y1="2" x2="18" y2="34"/>
      <line x1="2" y1="18" x2="34" y2="18"/>
      <path d="M5 10h26M5 26h26"/>
    </g>
  </svg>

  <p class="location">Alder Falls, AB</p>
  <div class="edge-bar"></div>
</section>

</body>
</html>
```